Free range pig farm business

We'd like a simple but elegant website for our new free range pig farm business.
Check out www.kellowridgeporkers.com.au and http://www.toravinefields.com.au/
pages:
Home
About
Shop
Contact
Target Market(s)
People who would want to find out where they could buy our pork
Industry/Entity Type
Agribusiness
Number of Pages Required
4 page
Font styles to use
Other font styles liked:
- As per our logo
Requirements
Must have
- Ability for us to update weekly with new news and photos

```html
<!DOCTYPE html>
<html lang="en">
<head>
<meta charset="utf-8">
<title>Greenhollow Pastured Pork</title>
<link href="https://fonts.googleapis.com/css2?family=Oswald:wght@300;400&family=Open+Sans:wght@400;600&family=Montserrat:wght@600&display=swap" rel="stylesheet">
<style>
:root{
  --lime:#8cc63f;
  --forest:#2b5726;
  --ink:#333;
  --muted:#8a8a8a;
  --grey-band:#efefef;
  --white:#fff;
  --rule:#e6e6e6;
}
*{box-sizing:border-box;margin:0;padding:0}
html,body{width:730px;height:1200px;overflow:hidden;background:var(--white)}
body{position:relative;font-family:'Open Sans',sans-serif;color:var(--ink)}
.abs{position:absolute}
.hero-backdrop{left:0;top:0;width:730px;height:343px;background:linear-gradient(180deg,#6a4536 0%,#8a5a3c 45%,#9c6a3a 75%,#5b3b24 100%)}
.grey-band{left:0;top:343px;width:730px;height:395px;background:var(--grey-band)}
.card{left:114px;top:0;width:502px;height:524px;background:var(--white);box-shadow:0 10px 14px -10px rgba(0,0,0,.35)}
.card-tab{left:139px;top:0;width:29px;height:2px;background:var(--lime)}
.nav{top:38px;font-family:'Oswald',sans-serif;font-weight:400;font-size:7.5px;letter-spacing:.3px;color:var(--forest);display:flex;gap:14px}
.nav .active{color:var(--lime)}
.brand{left:315px;top:22px;width:100px;text-align:center;font-family:'Oswald',sans-serif;font-size:7px;color:var(--forest);line-height:9px}
.brand .dot{display:block;width:22px;height:22px;border-radius:50%;background:var(--forest);margin:0 auto 4px}
.socials{display:flex;align-items:center;gap:4px;font-size:7px;color:#999}
.socials i{display:block;width:5px;height:5px;border-radius:50%;background:var(--forest)}
.hero{left:127px;top:78px;width:476px;height:222px;background:linear-gradient(160deg,#8aa060 0%,#b59878 35%,#7c6248 70%,#4f3d2c 100%);text-align:center;color:var(--white)}
.hero h1{margin-top:91px;font-family:'Open Sans',sans-serif;font-weight:400;font-size:17px;text-shadow:0 1px 3px rgba(0,0,0,.4)}
.hero h2{font-family:'Montserrat',sans-serif;font-weight:600;font-size:12px;text-shadow:0 1px 3px rgba(0,0,0,.4)}
.hero .cta{display:block;margin-top:56px;font-family:'Oswald',sans-serif;font-size:6.5px}
.rule{height:2px;background:var(--rule)}
.product{width:149px}
.photo{width:149px;height:86px}
.product h3,.news h3{font-family:'Oswald',sans-serif;font-weight:400;font-size:10px;color:var(--forest);margin-top:8px;line-height:13px}
.product p,.news p{font-size:6px;line-height:9.5px;color:var(--muted);margin-top:5px}
.price{font-family:'Oswald',sans-serif;font-weight:300;font-size:11px;color:var(--lime);margin-top:9px}
.btn{display:inline-block;background:var(--forest);color:var(--white);font-family:'Oswald',sans-serif;font-size:6.5px;padding:4px 10px;border:1px solid #1d3e19}
.btn.lit{background:var(--lime);border-color:var(--lime)}
.product .btn{margin-top:7px}
.arrow{width:13px;height:13px;border-radius:50%;top:405px;display:flex;align-items:center;justify-content:center}
.welcome-mark{left:127px;top:560px;width:150px;height:144px;display:flex;flex-direction:column;align-items:center;justify-content:center;gap:8px;font-family:'Oswald',sans-serif;font-size:11px;color:var(--forest);text-align:center}
.welcome-mark .dot{width:60px;height:60px;border-radius:50%;background:var(--forest)}
.divider{left:304px;top:558px;width:1px;height:146px;background:#d6d6d6}
.welcome{left:330px;top:564px;width:265px}
.welcome h2{font-family:'Oswald',sans-serif;font-weight:300;font-size:18px;color:var(--lime);line-height:20px}
.welcome h3{font-family:'Montserrat',sans-serif;font-weight:600;font-size:13px;color:var(--forest)}
.welcome p{font-size:6.4px;line-height:9.3px;color:var(--muted);margin-top:8px}
.welcome .btn{margin-top:19px}
.section-title{top:768px;left:0;width:730px;text-align:center;font-family:'Oswald',sans-serif;font-weight:300;font-size:19px;color:var(--lime)}
.news{width:150px}
.news .photo{width:150px;height:85px}
.news .date{font-family:'Oswald',sans-serif;font-size:6.5px;color:var(--lime);margin-top:8px}
.read{font-family:'Oswald',sans-serif;font-size:6.5px;color:var(--forest);margin-top:16px;display:flex;align-items:center;gap:4px}
.read i{width:6px;height:6px;border-radius:50%;background:var(--forest)}
.read.lit{color:var(--lime)}
.read.lit i{background:var(--lime)}
.strip{left:0;top:1042px;width:730px;height:106px;display:flex}
.strip div{flex:1}
.footer{top:1172px;left:127px;width:476px;display:flex;justify-content:space-between;align-items:center;font-size:6.5px;color:#666}
</style>
</head>
<body>
<div class="abs hero-backdrop" role="img" aria-label="Dusk farm landscape with mountains and an old truck"></div>
<div class="abs grey-band"></div>

<div class="abs card"></div>
<div class="abs card-tab"></div>
<nav class="abs nav" style="left:146px">
  <span class="active">HOME</span><span>ABOUT</span><span>GALLERY</span><span>SHOP</span><span>NEWS</span>
</nav>
<div class="abs brand"><span class="dot"></span>GREENHOLLOW PASTURED<br>PORK</div>
<div class="abs socials" style="left:433px;top:39px"><i></i>/<i></i>/<i></i>/<i></i>/<i></i></div>
<div class="abs nav" style="left:535px"><span>CONTACT</span></div>
<svg class="abs" style="left:576px;top:38px" width="8" height="8" viewBox="0 0 8 8"><circle cx="3.2" cy="3.2" r="2.3" fill="none" stroke="#2b5726" stroke-width="1.2"/><line x1="5" y1="5" x2="7.5" y2="7.5" stroke="#2b5726" stroke-width="1.3"/></svg>

<section class="abs hero" role="img" aria-label="Piglets rooting in a muddy paddock">
  <h1>Greenhollow Pastured Pork</h1>
  <h2>Free Range Pig Farm</h2>
  <span class="cta">SHOP PRODUCTS</span>
</section>
<div class="abs rule" style="left:127px;top:309px;width:476px"></div>

<div class="abs arrow" style="left:103px;background:#fff;box-shadow:0 0 3px rgba(0,0,0,.2)"><svg width="5" height="6" viewBox="0 0 5 6"><path d="M3.5 1 1.5 3l2 2" fill="none" stroke="#333" stroke-width="1"/></svg></div>
<div class="abs arrow" style="left:615px;background:var(--forest)"><svg width="5" height="6" viewBox="0 0 5 6"><path d="M1.5 1l2 2-2 2" fill="none" stroke="#fff" stroke-width="1"/></svg></div>

<article class="abs product" style="left:127px;top:324px">
  <div class="photo" role="img" aria-label="Cured pork cheek on paper" style="background:linear-gradient(135deg,#d8d2c8,#8b857d 60%,#cfc7bb)"></div>
  <h3>Guanciale</h3>
  <p>Guanciale is the Italian term for jowl or cheek. The pork cheek is cured with salt, ...</p>
  <div class="price">$10.00</div>
  <span class="btn">SHOP NOW</span>
</article>
<article class="abs product" style="left:290px;top:324px">
  <div class="photo" role="img" aria-label="Half ham on the bone on paper" style="background:linear-gradient(135deg,#c9c2b6,#d59a7c 50%,#8d8578)"></div>
  <h3>Half ham on the bone</h3>
  <p>Our hams are individually handcrafted on our farm from our free range Berkshire pigs.</p>
  <div class="price">$30.00</div>
  <span class="btn lit">SHOP NOW</span>
</article>
<article class="abs product" style="left:454px;top:324px">
  <div class="photo" role="img" aria-label="Sliced salami on wooden boards" style="background:linear-gradient(135deg,#9a948c,#6e4a52 55%,#c9c3b9)"></div>
  <h3>Swinefair Salami Competition Entry</h3>
  <p>Amateur and skilled traditionalist are urged to enter their salami's in the competition.</p>
  <div class="price">$15.00</div>
  <span class="btn">SHOP NOW</span>
</article>
<div class="abs rule" style="left:127px;top:512px;width:476px"></div>

<div class="abs welcome-mark"><span class="dot"></span>GREENHOLLOW<br>PASTURED PORK</div>
<div class="abs divider"></div>
<section class="abs welcome">
  <h2>Welcome to</h2>
  <h3>Greenhollow Pastured Pork</h3>
  <p>Lorem Ipsum is simply dummy text of the printing and typesetting industry. Lorem Ipsum has been the industry's standard dummy text ever since the 1500s, when an unknown printer took a galley of type and scrambled it to make a type specimen book. It has survived not only five centuries, but also the leap into electronic typesetting remaining essentially unchanged.</p>
  <span class="btn">DISCOVER MORE</span>
</section>

<h2 class="abs section-title">Latest News &amp; Updates</h2>
<article class="abs news" style="left:127px;top:806px">
  <div class="photo" role="img" aria-label="Cured meat being sliced, green overlay" style="background:linear-gradient(135deg,#4f6b3c,#6f8a4f)"></div>
  <h3>Charcuterie &amp; curing workshop- the essentials in meat preservation</h3>
  <div class="date">Sep14, 2016</div>
  <p>Lorem Ipsum has been the industry's standard dummy text ever since the 1500s, when an unknown printer took a galley of type and scrambled it to make a type specimen book.</p>
  <div class="read"><i></i>Read More</div>
</article>
<article class="abs news" style="left:290px;top:806px">
  <div class="photo" role="img" aria-label="Piglets around a boot on grass" style="background:linear-gradient(180deg,#7b7468,#c8b6a8 55%,#5f9a3f)"></div>
  <h3>Swinefair 2016 and new retail outlet in stony creek</h3>
  <div class="date">Sep 11, 2016</div>
  <p>Lorem Ipsum has been the industry's standard dummy text ever since the 1500s, when an unknown printer took a galley of type and scrambled it to make a type specimen book.</p>
  <div class="read lit"><i></i>Read More</div>
</article>
<article class="abs news" style="left:453px;top:806px">
  <div class="photo" role="img" aria-label="Sliced cured meat on a board" style="background:linear-gradient(135deg,#6a2a2e,#b5364a 50%,#c9a47a)"></div>
  <h3>Swinefair 2016 and new retail outlet in stony creek</h3>
  <div class="date">Sep 03, 2016</div>
  <p>Lorem Ipsum has been the industry's standard dummy text ever since the 1500s, when an unknown printer took a galley of type and scrambled it to make a type specimen book.</p>
  <div class="read"><i></i>Read More</div>
</article>

<div class="abs strip">
  <div role="img" aria-label="Black piglets huddled in straw" style="background:linear-gradient(135deg,#2a2c38,#6a6c78)"></div>
  <div role="img" aria-label="Child holding a piglet" style="background:linear-gradient(135deg,#8a6a58,#d89aa0)"></div>
  <div role="img" aria-label="Hands holding grain" style="background:linear-gradient(135deg,#2a2a2a,#9a9080)"></div>
  <div role="img" aria-label="People in a paddock, green overlay" style="background:linear-gradient(135deg,#4c6e3a,#6f8d55)"></div>
  <div role="img" aria-label="Hands holding cured meat, black and white" style="background:linear-gradient(135deg,#5a5a5a,#c8c8c8)"></div>
</div>

<footer class="abs footer">
  <span>© Greenhollow Pastured Pork 2016 . All Rights Reserved</span>
  <span class="socials"><i></i>/<i></i>/<i></i>/<i></i>/<i></i></span>
</footer>
</body>
</html>
```